Design some Business Cards for Kestrel spirits

Design a business card for Kestrel spirits

We are a small high end Kestrel spirits Company, we make Vodka, Gin, Rums and other stuff

Create front & back business card using theme colours logo supplied, needs to have the following details:

Name
Tittle

Phone number
Fax number
Mobile number
email
website kestrelspirits.com

Address

300 dpi and resolution of 3000 in the following format:
EPS
JPEG
PDF
PNG
PSD

We will be using http://www.plavo-press.com.hk/en/finishing.htm for printing of business cards, so any "Goldstamping" or "Embossing" needs to be in there format for the printers

We have over 30 brands which will need logos, so whoever wins this one will be invited back for them first

```html
<!DOCTYPE html>
<html lang="en">
<head>
<meta charset="utf-8">
<title>Kestrel Spirits — Business Card</title>
<link rel="stylesheet" href="https://fonts.googleapis.com/css2?family=Cinzel:wght@600&family=Arimo:wght@400;700&display=swap">
<style>
  :root {
    --stage: #e9e6e2;
    --card-dark-top: #0d0705;
    --card-dark-mid: #2a1208;
    --card-dark-bottom: #7a4510;
    --brand-red: #d8452c;
    --accent-orange: #e8501f;
    --ink: #1c1c1c;
    --ink-soft: #4a4a4a;
    --paper: #ffffff;
    --faint-brand: #e9c3bd;
    --band-red: #c5301d;
    --band-dark: #2a1a16;
    --ornament-gold: #c89a55;
  }
  * { box-sizing: border-box; margin: 0; padding: 0; }
  html, body { width: 1200px; height: 909px; overflow: hidden; }
  body { background: var(--stage); position: relative; }

  .card {
    position: absolute;
    left: 235px;
    width: 730px;
    height: 400px;
    overflow: hidden;
    box-shadow: 0 6px 18px rgba(0,0,0,0.18);
  }

  /* Front side */
  .card-front {
    top: 36px;
    background: radial-gradient(ellipse 70% 60% at 60% 100%, var(--card-dark-bottom) 0%, var(--card-dark-mid) 55%, var(--card-dark-top) 100%);
  }
  .brand-lockup {
    position: absolute;
    left: 0; right: 0; top: 70px;
    text-align: center;
  }
  .brand-name {
    font-family: "Cinzel", serif;
    font-weight: 600;
    color: var(--brand-red);
    font-size: 62px;
    letter-spacing: 2px;
    line-height: 1.15;
  }
  .brand-ornament {
    display: block;
    margin: 26px auto 0;
    width: 200px;
    height: 70px;
    border-radius: 50%;
    background: radial-gradient(ellipse at center, var(--ornament-gold) 0%, rgba(200,154,85,0.35) 55%, rgba(200,154,85,0) 75%);
  }

  /* Back side */
  .card-back {
    top: 473px;
    background: var(--paper);
  }
  .back-brand {
    position: absolute;
    left: 54px; top: 56px;
    font-family: "Cinzel", serif;
    font-weight: 600;
    font-size: 58px;
    color: var(--faint-brand);
    letter-spacing: 1px;
  }
  .contact {
    position: absolute;
    left: 410px; top: 130px;
    font-family: "Arimo", sans-serif;
    color: var(--ink);
  }
  .contact-name {
    font-weight: 700;
    font-size: 34px;
    color: var(--accent-orange);
    line-height: 1;
  }
  .contact-title {
    font-size: 19px;
    color: var(--ink-soft);
    margin-top: 4px;
    margin-bottom: 22px;
  }
  .contact-line {
    font-size: 17px;
    line-height: 1.55;
  }
  .edge-band {
    position: absolute;
    left: 0; bottom: 0;
    width: 730px; height: 90px;
  }
</style>
</head>
<body>

  <section class="card card-front" aria-label="Card front">
    <div class="brand-lockup">
      <h1 class="brand-name">Kestrel<br>Spirits</h1>
      <span class="brand-ornament" role="img" aria-label="Gold ornamental flourish"></span>
    </div>
  </section>

  <section class="card card-back" aria-label="Card back">
    <div class="back-brand" aria-hidden="true">Kestrel</div>

    <div class="contact">
      <p class="contact-name">Administrator</p>
      <p class="contact-title">Manager, CEO</p>
      <p class="contact-line">01870352</p>
      <p class="contact-line">9826705418</p>
      <p class="contact-line">hello@kestrelspirits.com</p>
      <p class="contact-line">www.kestrelspirits.com</p>
    </div>

    <svg class="edge-band" viewBox="0 0 730 90" preserveAspectRatio="none" aria-hidden="true">
      <path d="M0 40 C 200 55, 400 70, 730 82 L 730 90 L 0 90 Z" fill="var(--band-dark)"/>
      <path d="M0 30 C 180 44, 380 60, 560 70 C 420 70, 200 66, 0 62 Z" fill="var(--band-red)"/>
      <path d="M0 66 C 200 72, 420 78, 730 86" stroke="var(--band-red)" stroke-width="2" fill="none"/>
    </svg>
  </section>

</body>
</html>
```